Landcape Construction Company needs a flyer to catch attention

A flyer that can be displayed at several different stores detailing our skills, work produced, experience and contact details. Information can be extracted from our website www.brvkw.co.nz. The flyer should feel very green, with addition of pics of work completed as well as stock images of lush green plants, lawns, landscape or similar. Needs to be eye catching with just enough information to express our experience and commitment to high standards

Target Market(s)

Residential
Landscape Architects

Industry/Entity Type

Landscaping

Font styles to use
Serif

Colors
abd037

Requirements
Must have
• Our logo
Experience
Services offered including pictures
All information avail on our website www.brvkw.co.nz
Nice to have
• stock images of lush greenery like a garden after fresh rainfall
Should not have
• Nothing comes to mind

```html
<!DOCTYPE html>
<html lang="en">
<head>
<meta charset="utf-8">
<title>Brookvale Garden Works – Flyer</title>
<link href="https://fonts.googleapis.com/css2?family=Open+Sans:wght@400;600;700&family=Oswald:wght@500;600&display=swap" rel="stylesheet">
<style>
  :root {
    --bg: #e9e9e7;
    --white: #ffffff;
    --green-light: #8dc63f;
    --green-mid: #7aaf38;
    --green-dark: #187a3f;
    --green-text: #1c7a3c;
    --body-text: #4a4a4a;
    --photo-a: #8a7a68;
    --photo-b: #6f8d4a;
  }
  * { margin: 0; padding: 0; box-sizing: border-box; }
  html, body { width: 996px; height: 1200px; overflow: hidden; background: var(--bg); }
  .flyer {
    position: absolute; left: 74px; top: 0; width: 848px; height: 1200px;
    background: var(--white); overflow: hidden;
    font-family: "Open Sans", Arial, sans-serif;
  }
  .hero-photo {
    position: absolute; left: 0; top: 0; width: 848px; height: 486px;
    background: linear-gradient(180deg, #c9d3d6 0%, #9b8a76 30%, #6e6456 50%, #557a3a 72%, #6e9d3c 100%);
  }
  .brand-tag {
    position: absolute; left: 564px; top: 0; width: 286px; height: 214px;
    background: var(--white); border-bottom: 12px solid var(--green-light);
    display: flex; flex-direction: column; align-items: center; justify-content: center; gap: 12px;
  }
  .brand-dot { width: 100px; height: 100px; border-radius: 50%; background: var(--green-light); }
  .brand-name {
    font-weight: 700; color: var(--green-text); font-size: 18px; line-height: 1.15; text-align: center;
  }
  .services {
    position: absolute; left: 0; top: 486px; width: 848px; height: 290px; display: flex;
  }
  .service-col {
    flex: 1; background: var(--green-light); color: var(--white);
    text-transform: uppercase; font-size: 23.5px; line-height: 30.5px; text-align: center;
    padding-top: 116px;
  }
  .service-col.mid { background: var(--green-mid); }
  .service-photo {
    position: absolute; top: 391px; width: 176px; height: 176px; border-radius: 50%;
    background: rgba(255,255,255,0.55); padding: 10px;
  }
  .service-photo span {
    display: block; width: 100%; height: 100%; border-radius: 50%; border: 3px solid var(--white);
    background: linear-gradient(160deg, var(--photo-a), var(--photo-b));
  }
  .service-photo.p2 span { background: linear-gradient(160deg, #6d7d52, #4e5358); }
  .service-photo.p3 span { background: linear-gradient(170deg, #9fb2bd, #8b8f8c); }
  .call-bar {
    position: absolute; left: 0; top: 776px; width: 848px; height: 71px; background: var(--green-dark);
    color: var(--white); display: flex; align-items: center; padding: 0 30px;
  }
  .call-bar svg { width: 34px; height: 46px; margin-right: 14px; }
  .call-label, .call-number { font-family: "Oswald", Arial, sans-serif; font-weight: 500; font-size: 40px; letter-spacing: 0.5px; }
  .call-number { margin-left: 24px; }
  .call-web { margin-left: auto; font-weight: 700; font-size: 27px; }
  .intro {
    position: absolute; left: 0; top: 870px; width: 848px; text-align: center;
    color: var(--green-text); font-weight: 700; font-size: 23.5px; line-height: 32px;
  }
  .years-badge {
    position: absolute; left: 54px; top: 943px; width: 186px; height: 186px; border-radius: 50%;
    background: var(--green-dark); color: var(--white); display: flex; flex-direction: column;
    align-items: center; justify-content: center; border: 6px solid var(--white);
    box-shadow: 0 0 0 4px var(--green-dark); text-transform: uppercase; font-weight: 700;
  }
  .years-badge .small { font-size: 15px; letter-spacing: 2px; }
  .years-badge .big {
    font-size: 31px; background: var(--white); color: var(--green-dark); width: 200px;
    text-align: center; margin: 8px 0; line-height: 44px;
  }
  .solution { position: absolute; left: 294px; top: 967px; width: 520px; }
  .solution h2 { color: var(--green-text); font-size: 17px; font-weight: 700; text-transform: uppercase; margin-bottom: 6px; }
  .solution p { color: var(--body-text); font-size: 18px; line-height: 24.5px; text-align: justify; }
  .grass {
    position: absolute; left: 0; top: 1112px; width: 848px; height: 88px;
    background: linear-gradient(180deg, rgba(120,190,50,0) 0%, #8cc63f 40%, #4f9a2a 100%);
  }
  .local-pill {
    position: absolute; left: 286px; top: 1119px; width: 397px; height: 40px; border-radius: 20px;
    background: var(--green-light); border: 3px solid var(--white); color: var(--white);
    font-weight: 700; font-size: 19px; text-align: center; line-height: 34px; text-transform: uppercase;
  }
</style>
</head>
<body>
<main class="flyer">
  <div class="hero-photo" role="img" aria-label="Modern two-storey home with landscaped garden, lawn and curved paved path"></div>

  <div class="brand-tag">
    <div class="brand-dot"></div>
    <div class="brand-name">The Brookvale Garden<br>Works Company Ltd</div>
  </div>

  <section class="services">
    <div class="service-col">Patios<br>Paving<br>Concrete<br>Water Features<br>Decking</div>
    <div class="service-col mid">Fencing<br>Boardwalks<br>Timber<br>Planter Boxes<br>Pergolas</div>
    <div class="service-col">Retaining Walls<br>Gardens &amp; Lawns<br>Irrigation<br>Project Management<br>Consultation</div>
  </section>
  <div class="service-photo" style="left:52px" role="img" aria-label="Timber slat fence"><span></span></div>
  <div class="service-photo p2" style="left:338px" role="img" aria-label="Paved patio with outdoor seating"><span></span></div>
  <div class="service-photo p3" style="left:635px" role="img" aria-label="Stone paving overlooking water"><span></span></div>

  <div class="call-bar">
    <svg viewBox="0 0 34 46" aria-hidden="true">
      <rect x="6" y="2" width="22" height="40" rx="4" fill="none" stroke="#fff" stroke-width="3"/>
      <line x1="13" y1="36" x2="21" y2="36" stroke="#fff" stroke-width="3"/>
      <path d="M2 20 q-2 14 10 24 l8 0 q-4-8 -4-14 q-8 -4 -14 -10z" fill="#fff"/>
    </svg>
    <span class="call-label">CALL US NOW!!!</span>
    <span class="call-number">021 448 752</span>
    <span class="call-web">www.brvkw.co.nz</span>
  </div>

  <p class="intro">The Brookvale Garden Works Company offers services to large or small<br>residential and commercial projects.</p>

  <div class="years-badge">
    <span class="small">Experience</span>
    <span class="big">25 Years</span>
    <span class="small">Experience</span>
  </div>

  <div class="solution">
    <h2>The best solution to your landscaping needs.!</h2>
    <p>Whether you have a blank canvas or are looking to rejuvinate your property we are able to advise and make the process easy and stress free. From paving, pergolas and decks to concrete or planting your dream garden we have the expertise to help.</p>
  </div>

  <div class="grass" role="img" aria-label="Fresh green lawn grass along the bottom edge"></div>
  <div class="local-pill">Locally owned and operated</div>
</main>
</body>
</html>
```